Property investment company needs a letterhead design!

We are a new residential and commercial property investment company. Name of the company is Morvesta Group, LLC. We have a new logo and now we need letterhead! We prefer to have a professional and upscale appearance. We don't have any fixed requirements, so be creative! Thank you for considering this project. We are so excited to see what happens!

Target Market(s)

Professional

Industry/Entity Type

Real Estate Development

```html
<!DOCTYPE html>
<html lang="en">
<head>
<meta charset="utf-8">
<title>Morvesta Group, LLC — Letterhead</title>
<link href="https://fonts.googleapis.com/css2?family=Open+Sans:wght@400;600&display=swap" rel="stylesheet">
<style>
  :root {
    --brand-blue: #00aeef;
    --brand-navy: #263550;
    --ink: #1c1c1c;
    --muted-blue: #3e5a82;
    --paper: #ffffff;
    --backdrop: #e4e4e4;
  }
  * { margin: 0; padding: 0; box-sizing: border-box; }
  html, body {
    width: 1200px; height: 2292px; overflow: hidden;
    background: var(--backdrop);
    font-family: "Open Sans", Arial, sans-serif;
  }
  .letterhead {
    position: absolute; left: 40px; top: 353px;
    width: 956px; height: 1353px;
    background: var(--paper);
    transform: scale(1.1715); transform-origin: top left;
    box-shadow: 0 8px 22px rgba(0,0,0,.28);
    overflow: hidden;
  }
  .sheet-shapes { position: absolute; inset: 0; }
  .brand {
    position: absolute; left: 74px; top: 186px;
    display: flex; align-items: center; gap: 14px;
  }
  .brand-dot {
    width: 44px; height: 44px; border-radius: 50%;
    background: var(--brand-blue);
  }
  .brand-name {
    font-size: 30px; font-weight: 600; color: var(--brand-navy);
    letter-spacing: .5px;
  }
  .subject {
    position: absolute; left: 73px; top: 382px;
    font-size: 34px; font-weight: 400; color: var(--ink);
  }
  .body-copy {
    position: absolute; left: 73px; top: 458px; width: 809px;
    font-size: 18.6px; line-height: 25.5px; color: var(--ink);
    text-align: justify;
  }
  .body-copy p + p { margin-top: 25px; }
  .signoff {
    position: absolute; right: 65px; top: 1078px; text-align: right;
  }
  .signature-mark {
    width: 120px; height: 30px; margin-left: auto;
    background: linear-gradient(90deg, rgba(28,28,28,.05), rgba(28,28,28,.18));
    border-radius: 4px;
  }
  .signer-name { font-size: 17px; color: var(--muted-blue); margin-top: 12px; }
  .signer-title { font-size: 13px; color: var(--muted-blue); }
  .contact {
    position: absolute; color: #fff; font-size: 19px; line-height: 31px;
    display: flex; flex-direction: column;
  }
  .contact-line { display: flex; align-items: center; gap: 8px; }
  .contact-line svg { width: 20px; height: 20px; flex: none; }
  .contact--phone { left: 116px; top: 1260px; font-weight: 600; }
  .contact--online { left: 403px; top: 1253px; }
  .contact--address { left: 704px; top: 1253px; line-height: 25px; }
  .contact--address .contact-line { align-items: flex-start; }
</style>
</head>
<body>
<main class="letterhead">
  <svg class="sheet-shapes" viewBox="0 0 956 1353" width="956" height="1353" aria-hidden="true">
    <polygon class="header-band" points="0,0 956,0 956,143 413,143 318,45 0,45" fill="var(--brand-blue)"/>
    <polygon class="header-bar" points="0,58 300,58 333,90 0,90" fill="var(--brand-navy)"/>
    <polygon class="footer-accent" points="491,1198 956,1198 956,1230 465,1230" fill="var(--brand-blue)"/>
    <polygon class="footer-base" points="413,1230 956,1230 956,1353 0,1353 0,1326 331,1326" fill="var(--brand-navy)"/>
    <polygon class="footer-phone-tab" points="101,1233 391,1233 321,1318 34,1318" fill="var(--brand-blue)"/>
  </svg>

  <div class="brand">
    <span class="brand-dot"></span>
    <span class="brand-name">MORVESTA GROUP, LLC</span>
  </div>

  <h1 class="subject">SUBJECT HERE</h1>

  <section class="body-copy">
    <p>Lorem ipsum, or lipsum as it is sometimes known, is dummy text used in laying out print, graphic or web designs. The passage is attributed to an unknown typesetter in the 15th century who is thought to have scrambled parts of Cicero's De Finibus Bonorum et Malorum for use in a type specimen book. It usually begins with. Lorem ipsum, or lipsum as it is sometimes known, is dummy text used in laying out print, graphic or web designs. The passage is attributed to an unknown typesetter in the 15th century who is thought to have scrambled parts of Cicero's De Finibus Bonorum et Malorum for use in a type specimen book. It usually begins with.</p>
    <p>Lorem ipsum, or lipsum as it is sometimes known, is dummy text used in laying out print, graphic or web designs. The passage is attributed to an unknown typesetter in the 15th century who is thought to have scrambled parts of Cicero's De Finibus Bonorum et Malorum for use in a type specimen book. It usually begins with. Lorem ipsum, or lipsum as it is sometimes known, is dummy text used in laying out print, graphic or web designs. The passage is attributed to an unknown typesetter in the 15th century who is thought to have scrambled parts of Cicero's De Finibus Bonorum et Malorum for use in a type specimen book. It usually begins with. Lorem ipsum, or lipsum as it is sometimes known, is dummy text used in laying out print, graphic or web designs. The passage is attributed to an unknown typesetter in the 15th century who is thought to have scrambled parts of Cicero's De Finibus Bonorum et Malorum for use in a type specimen book. It usually begins with. Lorem ipsum, or lipsum as it is sometimes known, is dummy text used in laying out print, graphic or web designs. The passage is attributed to an unknown typesetter.</p>
  </section>

  <div class="signoff">
    <div class="signature-mark" role="img" aria-label="Handwritten signature"></div>
    <div class="signer-name">LOREM IPSUM</div>
    <div class="signer-title">Lorem Ipsum</div>
  </div>

  <div class="contact contact--phone">
    <span class="contact-line">
      <svg viewBox="0 0 24 24" aria-hidden="true"><path fill="var(--brand-navy)" d="M6.6 10.8a15 15 0 0 0 6.6 6.6l2.2-2.2a1 1 0 0 1 1-.25 11.4 11.4 0 0 0 3.6.57 1 1 0 0 1 1 1V20a1 1 0 0 1-1 1A17 17 0 0 1 3 4a1 1 0 0 1 1-1h3.5a1 1 0 0 1 1 1c0 1.25.2 2.45.57 3.57a1 1 0 0 1-.25 1z"/></svg>
      (555) 318-0274
    </span>
  </div>

  <div class="contact contact--online">
    <span class="contact-line">
      <svg viewBox="0 0 24 24" aria-hidden="true"><rect x="2" y="5" width="20" height="14" rx="1" fill="var(--brand-blue)"/><path d="M2.5 5.5 12 13l9.5-7.5" fill="none" stroke="var(--brand-navy)" stroke-width="1.6"/></svg>
      MorvestaLLC@mailbox.com
    </span>
    <span class="contact-line">
      <svg viewBox="0 0 24 24" aria-hidden="true"><g fill="none" stroke="var(--brand-blue)" stroke-width="1.8"><circle cx="12" cy="12" r="9"/><ellipse cx="12" cy="12" rx="4" ry="9"/><path d="M3 12h18M5 7h14M5 17h14"/></g></svg>
      www.Morvesta.com
    </span>
  </div>

  <div class="contact contact--address">
    <span class="contact-line">
      <svg viewBox="0 0 24 24" aria-hidden="true"><path fill="var(--brand-blue)" d="M12 2a7 7 0 0 0-7 7c0 5 7 13 7 13s7-8 7-13a7 7 0 0 0-7-7zm0 9.5A2.5 2.5 0 1 1 12 6.5a2.5 2.5 0 0 1 0 5z"/></svg>
      <span>1184 N. Alder Ave.<br>Pine Ridge, MI 49120</span>
    </span>
  </div>
</main>
</body>
</html>
```